Website design needed for gift based dropship website

I am building a dropshipping website that will create gift based merchandise and send it out to our clients customers for them. Our clients will sell products and when a customer buys from them, we create the item and send it out to the customer.

I am looking for a very similar website to brindlow.com - that website is doing a very similar thing to what i am doing but where the brindlow website is based around clothing, my website will be based around gifts. Another website that i like that is doing a similar thing to what i will do is vemtar.com

I require 2 pages to be made:
1) The home page
2) A landing page for a free product giveaway offer

1) THE HOME PAGE
The home page should be a merger of the two previously stated websites (www.vemtar.com and www.brindlow.com). The style fo the homepage should be based on the logo that is attached and the colour scheme should be similar but basic.

2) THE LANDING PAGE
The landing page will be giving away a free mobile phone cover. The page needs to have some mobile phone covers for different phones all with random designs on. The page should state that they can have any design that they want and they do not pay for the phone (they only pay for shipping).

Menu pages and text should be taken from the brindlow.com website.

18 - 40 year old males. People who like the idea of earning extra money in their spare time but aren't too sure how to do it. Semi-professional jobs.

2 page

• A "how it works" image where the dropshipping process is explained to a visitor to the website (similar to the one on the brindlow "how it works page")
• Testimonial area on homepage
• Homepage should not have:
• - "latest orders from" area
• - Video
• - Warehousing/fulfilment area
• - Integration area
• -

```html
<!DOCTYPE html>
<html lang="en">
<head>
<meta charset="utf-8">
<title>Parcelle Prints – Sell Gift Online</title>
<link href="https://fonts.googleapis.com/css2?family=Oswald:wght@400;500;600;700&family=Roboto:wght@400;500;700&display=swap" rel="stylesheet">
<style>
:root{
  --red:#e8392a;
  --maroon:#5a1425;
  --maroon-dark:#4a1020;
  --ink:#2b2b2b;
  --muted:#666;
  --soft:#f4f4f4;
  --line:#e3e3e3;
  --stone:#cfc8c6;
  --white:#fff;
  --star:#f2b01e;
}
*{box-sizing:border-box;margin:0;padding:0}
html,body{width:1200px;height:3000px;overflow:hidden;background:var(--white)}
body{position:relative;font-family:'Roboto',Arial,sans-serif;color:var(--ink)}
.abs{position:absolute}
.heading{font-family:'Oswald','Arial Narrow',sans-serif;font-weight:500;text-transform:uppercase;text-align:center;font-size:30px;color:var(--ink)}
.heading .accent{color:var(--red)}

/* top bar */
.topbar{top:0;left:0;width:1200px;height:20px;border-bottom:1px solid var(--line);font-size:10px;font-weight:500}
.topbar .promo{left:160px;top:4px}
.topbar .ads{left:954px;top:4px;display:flex;gap:6px;align-items:center}

/* header */
.header{top:20px;left:0;width:1200px;height:56px;border-bottom:3px solid var(--maroon)}
.phone{left:160px;top:17px;display:flex;gap:10px;align-items:center;font-size:12px;font-weight:700}
.brand{left:540px;top:6px;display:flex;align-items:center;gap:8px}
.brand-dot{width:34px;height:34px;border-radius:50%;background:var(--maroon)}
.brand-name{font-family:'Oswald',sans-serif;font-weight:600;font-size:20px;line-height:20px;color:var(--maroon);text-transform:uppercase;width:90px}
.search{left:864px;top:10px;width:176px;height:28px;border:1px solid #ccc;display:flex;justify-content:flex-end;align-items:center;padding-right:8px}

/* nav */
.nav{top:79px;left:0;width:1200px;height:31px}
.nav ul{position:absolute;left:160px;top:0;display:flex;list-style:none;font-size:10px;font-weight:500;text-transform:uppercase}
.nav li{padding:9px 16px 0;height:31px;color:#333}
.nav li.active{color:var(--red);border-bottom:2px solid var(--red)}
.get-started{left:968px;top:9px;font-size:10px;font-weight:700;color:var(--red);display:flex;gap:8px;align-items:center}

/* hero */
.hero{top:110px;left:0;width:1200px;height:534px;background:radial-gradient(ellipse at 50% 40%,#f3ecec 0%,#f2dcdc 45%,#e9c2c2 100%)}
.hero-title{top:346px;left:0;width:1200px;text-align:center;font-family:'Oswald',sans-serif;font-weight:700;font-size:66px;line-height:84px;color:var(--maroon-dark);text-transform:uppercase;letter-spacing:-1px}
.hero-sub{top:440px;left:0;width:1200px;text-align:center;font-size:14px;font-weight:700;line-height:20px;color:#222}
.hero-btn{top:500px;left:536px;width:128px;height:40px;background:var(--white);font-size:11px;font-weight:700;display:flex;align-items:center;justify-content:center;box-shadow:0 1px 3px rgba(0,0,0,.15)}
.hero-notch{top:628px;left:580px}

/* products */
.products{top:644px;left:0;width:1200px;height:566px;background:var(--soft)}
.products .heading{position:absolute;top:62px;width:1200px}
.card{position:absolute;width:240px;text-align:center}
.card .photo{width:240px;height:268px}
.card .title{margin-top:14px;font-family:'Oswald',sans-serif;font-size:14px;color:var(--ink)}
.card .title span{color:#999}
.card .desc{margin-top:6px;font-size:10px;color:var(--muted)}
.price{display:inline-block;margin-top:14px;background:var(--red);color:var(--white);font-size:10px;font-weight:700;padding:4px 16px}
.price b{font-size:12px;margin-left:8px}
.arrow{position:absolute;width:22px;height:22px;border-radius:50%;display:flex;align-items:center;justify-content:center}
.arrow.prev{background:#f3a9a0}
.arrow.next{background:var(--maroon)}

/* how it works */
.how{top:1280px;left:204px;width:792px;height:510px;border:8px solid #f1f1f1}
.how .heading{position:absolute;top:24px;left:0;width:776px}
.step{position:absolute}
.step-num{position:absolute;top:0;right:0;width:48px;height:52px;background:#fbeeee;font-family:'Oswald',sans-serif;font-size:26px;display:flex;align-items:center;justify-content:center;color:#222}
.step-btn{position:absolute;background:var(--maroon);color:var(--white);font-size:9px;font-weight:700;display:flex;justify-content:space-between;align-items:center;padding:0 10px;height:20px}
.step-btn.light{background:var(--white);color:var(--maroon)}
.step-label{font-size:10px;color:#333;text-align:center;line-height:18px}
.step-title{font-family:'Oswald',sans-serif;font-size:15px;color:var(--maroon)}

/* testimonials */
.rule{left:0;width:1200px;height:2px;background:#eee}
.clients .heading{position:absolute;top:1890px;left:0;width:1200px}
.clients .sub{position:absolute;top:1934px;left:0;width:1200px;text-align:center;font-size:11px;color:#444}
.quote{position:absolute;top:1980px;width:240px;text-align:center}
.quote .photo{height:230px}
.stars{margin-top:10px;color:var(--star);font-size:17px;letter-spacing:1px}
.stars .off{color:#ccc}
.quote p{margin-top:4px;font-size:10px;line-height:12px;text-transform:uppercase;color:#333}
.more{display:inline-block;margin-top:10px;background:var(--red);color:var(--white);font-size:10px;font-weight:700;padding:4px 18px}

/* signup */
.signup{top:2430px;left:204px;width:792px;height:120px;border:2px solid #eee;display:flex;align-items:center;padding:0 18px}
.signup h3{font-family:'Oswald',sans-serif;font-weight:500;font-size:24px;line-height:28px;color:var(--red);text-transform:uppercase;width:220px}
.field{width:216px;height:46px;border:1px solid #ddd;font-size:11px;color:#999;padding:15px 14px;margin-right:10px}
.signup-btn{width:104px;height:46px;background:var(--red);color:var(--white);font-size:13px;font-weight:700;display:flex;align-items:center;justify-content:center}

/* footer */
.footer{top:2604px;left:0;width:1200px;height:260px;background:var(--soft)}
.footer .brand{left:160px;top:28px}
.footer-about{left:160px;top:88px;width:410px;font-size:10px;line-height:14px;color:#333}
.footer-col{position:absolute;top:52px;font-size:10px;line-height:20px;color:#333;list-style:none}
.footer-col h4{font-family:'Oswald',sans-serif;font-weight:500;font-size:15px;color:var(--maroon);margin-bottom:8px;line-height:20px}
.footer-legal{top:2886px;left:160px;width:880px;text-align:center;font-size:10px;line-height:16px;color:#333}
.bottombar{top:2964px;left:0;width:1200px;height:36px;background:var(--maroon-dark);color:var(--white);font-size:10px}
.bottombar .copy{position:absolute;left:160px;top:12px}
.social{position:absolute;left:944px;top:9px;display:flex;gap:14px}
.social span{width:18px;height:18px;border-radius:50%;background:rgba(255,255,255,.85)}
</style>
</head>
<body>

<div class="abs topbar">
  <div class="abs promo">Free Shipping on most* $50+ orders</div>
  <div class="abs ads">
    <svg width="9" height="12" viewBox="0 0 9 12"><path d="M4.5 0C2 0 0 2 0 4.5 0 8 4.5 12 4.5 12S9 8 9 4.5C9 2 7 0 4.5 0zm0 6.3a1.8 1.8 0 110-3.6 1.8 1.8 0 010 3.6z" fill="#222"/></svg>
    Shop current ads
  </div>
</div>

<header class="abs header">
  <div class="abs phone">
    <svg width="14" height="14" viewBox="0 0 24 24"><path d="M6.6 10.8a15 15 0 006.6 6.6l2.2-2.2c.3-.3.7-.4 1-.2 1.1.4 2.3.6 3.6.6.6 0 1 .4 1 1V20c0 .6-.4 1-1 1A17 17 0 013 4c0-.6.4-1 1-1h3.5c.6 0 1 .4 1 1 0 1.3.2 2.5.6 3.6.1.3 0 .7-.2 1z" fill="#e8392a"/></svg>
    555 018 2746
  </div>
  <div class="abs brand">
    <span class="brand-dot"></span>
    <span class="brand-name">Parcelle Prints</span>
  </div>
  <div class="abs search">
    <svg width="14" height="14" viewBox="0 0 14 14"><circle cx="6" cy="6" r="4.5" fill="none" stroke="#999" stroke-width="1.6"/><line x1="9.3" y1="9.3" x2="13" y2="13" stroke="#999" stroke-width="1.8"/></svg>
  </div>
</header>

<nav class="abs nav">
  <ul>
    <li class="active">Pricing</li>
    <li>How It Works</li>
    <li>Resources</li>
    <li>Mock Up Generator</li>
    <li>FAQ</li>
    <li>Blogs</li>
    <li>Contact Us</li>
  </ul>
  <div class="abs get-started">
    <svg width="14" height="11" viewBox="0 0 14 11"><rect x="0.5" y="0.5" width="13" height="10" rx="1" fill="none" stroke="#e8392a"/><path d="M1 1l6 5 6-5" fill="none" stroke="#e8392a"/></svg>
    Get Started
  </div>
</nav>

<section class="abs hero" role="img" aria-label="Smiling woman in a knit hat holding a wrapped gift, surrounded by floating red gift boxes"></section>
<h1 class="abs hero-title">Sell Gift Online</h1>
<p class="abs hero-sub">If you want to sell your designs in an online<br>store or marketplace</p>
<div class="abs hero-btn">Connect Your Shop</div>
<svg class="abs hero-notch" width="40" height="16" viewBox="0 0 40 16"><path d="M0 0h40L20 16z" fill="#d9c9c9"/></svg>

<section class="abs products">
  <h2 class="heading">Our <span class="accent">Products</span></h2>
  <div class="arrow prev" style="left:186px;top:306px"><svg width="8" height="8" viewBox="0 0 8 8"><path d="M6 4H1M3.5 1.5L1 4l2.5 2.5" stroke="#fff" stroke-width="1.3" fill="none"/></svg></div>
  <div class="arrow next" style="left:986px;top:306px"><svg width="8" height="8" viewBox="0 0 8 8"><path d="M1 4h5M4.5 1.5L7 4 4.5 6.5" stroke="#fff" stroke-width="1.3" fill="none"/></svg></div>

  <div class="card" style="left:224px;top:140px">
    <div class="photo" role="img" aria-label="Stack of colourful wrapped gift boxes with ribbons" style="background:linear-gradient(160deg,#f4f4f4,#e2e2e2 60%,#c63a3a 100%)"></div>
    <div class="title"><span>Lorem Ipsum Dolor</span> Sit Amet Consect</div>
    <div class="desc">Lorem Ipsum Dolor Sit Amet Consectetor</div>
    <div class="price">From <b>$20.00</b></div>
  </div>
  <div class="card" style="left:478px;top:140px">
    <div class="photo" role="img" aria-label="Hands holding a gold gift box with a red bow on a teal background" style="background:radial-gradient(circle at 50% 55%,#d9a84a 0%,#c9463d 22%,#7fcfc4 45%,#79c9bf 100%)"></div>
    <div class="title"><span>Lorem Ipsum Dolor</span> Sit Amet Consect</div>
    <div class="desc">Lorem Ipsum Dolor Sit Amet Consectetor</div>
    <div class="price">From <b>$20.00</b></div>
  </div>
  <div class="card" style="left:734px;top:140px">
    <div class="photo" role="img" aria-label="Woman in a red festive sweater holding a gold gift box" style="background:linear-gradient(180deg,#dedede 0%,#d6d2d0 45%,#b52a2e 100%)"></div>
    <div class="title"><span>Lorem Ipsum Dolor</span> Sit Amet Consect</div>
    <div class="desc">Lorem Ipsum Dolor Sit Amet Consectetor</div>
    <div class="price" style="margin-top:28px">From <b>$20.00</b></div>
  </div>
</section>

<section class="abs how">
  <h2 class="heading"><span class="accent">How It</span> Works</h2>

  <div class="step" style="left:26px;top:86px;width:234px;height:232px;background:var(--red)">
    <div class="step-num">1</div>
    <svg class="abs" style="left:95px;top:86px" width="44" height="50" viewBox="0 0 44 50"><circle cx="22" cy="12" r="9" fill="#fff"/><path d="M8 40c0-9 6-15 14-15s14 6 14 15z" fill="#fff"/><path d="M2 36c6 6 12 10 20 10s14-4 20-10" stroke="#fff" stroke-width="4" fill="none"/></svg>
  </div>
  <div class="abs step-label" style="left:26px;top:336px;width:234px"><div class="step-title">Gerry</div><div style="margin-top:10px">Garry Buys Something At<br>our Store</div></div>
  <div class="step-btn" style="left:82px;top:432px;width:146px"><span>STEP - 1</span><span>→</span></div>

  <div class="step" style="left:290px;top:86px;width:226px;height:380px;background:var(--stone)">
    <div class="step-num" style="background:#f6f1f0">2</div>
    <svg class="abs" style="left:89px;top:162px" width="48" height="44" viewBox="0 0 48 44"><path d="M4 2h40l4 12H0z" fill="#5a1425"/><rect x="4" y="16" width="40" height="26" fill="#5a1425"/><rect x="12" y="22" width="10" height="20" fill="#cfc8c6"/><rect x="28" y="22" width="10" height="10" fill="#cfc8c6"/></svg>
    <div class="abs step-label" style="left:0;top:272px;width:226px">Order Get Sent Automati-<br>cally To Parcelle Prints</div>
    <div class="abs step-title" style="left:0;top:314px;width:226px;text-align:center">Your Store</div>
    <div class="step-btn" style="left:38px;top:348px;width:146px"><span>STEP - 2</span><span>→</span></div>
  </div>

  <div class="step" style="left:546px;top:86px;width:204px;height:178px;background:var(--stone)">
    <div class="step-num" style="background:#f6f1f0">3</div>
    <span class="abs" style="left:12px;top:28px;width:60px;height:52px;border-radius:50%;background:var(--maroon)"></span>
    <div class="abs step-label" style="left:10px;top:98px;text-align:left">Product Get Made</div>
    <div class="abs step-title" style="left:10px;top:118px">Parcelle Prints</div>
    <div class="step-btn light" style="left:10px;top:148px;width:92px"><span>STEP - 3</span><span>→</span></div>
  </div>

  <div class="step" style="left:546px;top:286px;width:204px;height:180px;background:var(--maroon)">
    <div class="step-num" style="background:#f6f1f0">4</div>
    <svg class="abs" style="left:12px;top:24px" width="52" height="40" viewBox="0 0 52 40"><rect x="2" y="4" width="8" height="36" fill="#fff"/><path d="M10 40V22l12-8v8l12-8v8l12-8v26z" fill="#fff"/></svg>
    <div class="abs step-label" style="left:10px;top:100px;color:#fff;text-align:left">Your Brands All Over It</div>
    <div class="abs step-title" style="left:10px;top:120px;color:#fff">Your Products</div>
    <div class="step-btn light" style="left:10px;top:148px;width:92px"><span>STEP - 4</span><span>→</span></div>
  </div>
</section>

<div class="abs rule" style="top:1850px"></div>

<section class="clients">
  <h2 class="heading"><span class="accent">What Our</span> Client Says</h2>
  <p class="sub">Lorem Ipsum Dolor Sit Amet Consectetor</p>
  <div class="arrow prev" style="left:188px;top:2124px"><svg width="8" height="8" viewBox="0 0 8 8"><path d="M6 4H1M3.5 1.5L1 4l2.5 2.5" stroke="#fff" stroke-width="1.3" fill="none"/></svg></div>
  <div class="arrow next" style="left:988px;top:2124px"><svg width="8" height="8" viewBox="0 0 8 8"><path d="M1 4h5M4.5 1.5L7 4 4.5 6.5" stroke="#fff" stroke-width="1.3" fill="none"/></svg></div>

  <div class="quote" style="left:226px">
    <div class="photo" role="img" aria-label="Client in a red festive sweater holding a gift" style="background:linear-gradient(180deg,#e0dcdb,#d4cfcd 50%,#b52a2e)"></div>
    <div class="stars">★★★★<span class="off">☆</span></div>
    <p>Lorem ipsum dolor sit amet consectetor<br>dolor sit amet</p>
    <div class="more">MORE</div>
  </div>
  <div class="quote" style="left:480px">
    <div class="photo" role="img" aria-label="Client holding a pink gift box against a pink backdrop" style="background:radial-gradient(circle at 50% 60%,#f0c8d2,#e58cac 55%,#d96e96)"></div>
    <div class="stars">★★★★<span class="off">☆</span></div>
    <p>Lorem ipsum dolor sit amet consectetor<br>dolor sit amet</p>
    <div class="more">MORE</div>
  </div>
  <div class="quote" style="left:734px">
    <div class="photo" role="img" aria-label="Client holding a stack of red gift boxes" style="background:linear-gradient(180deg,#eeeeee,#e6dede 50%,#d33a3e)"></div>
    <div class="stars">★★★★<span class="off">☆</span></div>
    <p>Lorem ipsum dolor sit amet consectetor<br>dolor sit amet</p>
    <div class="more">MORE</div>
  </div>
</section>

<div class="abs rule" style="top:2370px"></div>

<section class="abs signup">
  <h3>Create Your<br>Account For Free</h3>
  <div class="field">Email</div>
  <div class="field">Password</div>
  <div class="signup-btn">SIGN UP</div>
</section>

<footer class="abs footer">
  <div class="abs brand">
    <span class="brand-dot"></span>
    <span class="brand-name">Parcelle Prints</span>
  </div>
  <p class="abs footer-about">Lorem ipsum dolor sit amet, consectetur adipiscing elit, sed do eiusmod tempor incididunt ut labore et dolore magna aliqua. Ut enim ad minim veniam, quis nostrud exercitation ullamco laboris nisi ut aliquip ex ea commodo consequat. Lorem ipsum dolor sit amet, consectetur adipiscing elit, sed do eiusmod tempor incididunt ut labore et dolore magna aliqua. Ut enim ad minim veniam, quis nostrud exercitation ullamco laboris nisi ut aliquip ex ea commodo consequat.</p>
  <ul class="footer-col" style="left:636px"><h4>About Us</h4><li>About</li><li>Blog</li><li>Contact</li><li>Careers</li><li>Privacy</li><li>Terms</li></ul>
  <ul class="footer-col" style="left:746px;top:80px"><li>How IT Works</li><li>Products</li><li>Contact Us</li><li>Login</li></ul>
  <ul class="footer-col" style="left:938px"><h4>Parcelle Prints</h4><li>Pricing</li><li>How It Works</li><li>Resources</li><li>Mock Up Generator</li><li>FAQ</li><li>Blogs</li><li>Contact Us</li></ul>
</footer>

<p class="abs footer-legal">Lorem ipsum dolor sit amet, consectetur adipiscing elit, sed do eiusmod tempor incididunt ut labore et dolore magna aliqua.<br>Ut enim ad minim veniam, quis nostrud exercitation ullamco laboris nisi ut aliquip ex ea commodo consequat. Lorem ipsum dolor sit amet, consectetur adipiscing elit,<br>sed do eiusmod tempor incididunt ut labore et dolore magna aliqua. Ut enim ad minim veniam, quis nostrud exercitation ullamco laboris nisi ut aliquip ex ea commodo consequat.</p>

<div class="abs bottombar">
  <div class="copy">© Copyright 2018 Parcelle Prints, All Rights Reserved.</div>
  <div class="social"><span></span><span></span><span></span><span></span></div>
</div>

</body>
</html>
```